Business Card Design Project

We are a distribution company providing goods to Latin America. We sell everything from Medical equipment, generic medicines, to carecliners. The logo that we use is attached. The logo can incorporate different colors other than black for versatility. The company name is Valdoria International Corporation and/or VIC. The card will be printed using 1 or more of the following: Silk mounted and/or embossed. So if the design ideas could be made to incorporate that technique or any other unique techniques, it would be great. The target market is dialysis centers/doctors.

Basic Info for card:
Marnie Dowsett
Purchasing Manager
555-317-4086 direct
555-241-7953 fax
marnie.dowsett@valdoriavic.example
www.valdoriavic.example

Target Market(s)

Latin America

Industry/Entity Type

Business

Requirements
Nice to have
• The Front of the card should have the basic contact information with company name/logo. The back of the card could incorporate

```html
<!DOCTYPE html>
<html lang="en">
<head>
<meta charset="utf-8">
<title>Valdoria International Corporation – Business Card</title>
<link rel="stylesheet" href="https://fonts.googleapis.com/css2?family=Open+Sans:wght@400;600&family=Arimo:wght@400&display=swap">
<style>
  :root {
    --page-bg: #e9e6e2;
    --card-black: #050505;
    --stripe-red: #a8402c;
    --accent-red: #d7362a;
    --text-white: #ffffff;
    --text-grey: #a9a9a9;
    --shadow: rgba(0,0,0,0.35);
  }
  * { margin: 0; padding: 0; box-sizing: border-box; }
  html, body { width: 1200px; height: 741px; overflow: hidden; }
  body {
    background: var(--page-bg);
    position: relative;
    font-family: "Arimo", Arial, sans-serif;
  }
  .card {
    position: absolute;
    width: 540px;
    height: 309px;
    background: var(--card-black);
    box-shadow: 0 10px 24px var(--shadow);
    overflow: hidden;
  }
  .card--front { left: 40px; top: 216px; }
  .card--back {
    left: 620px; top: 216px;
    background:
      repeating-linear-gradient(160deg,
        var(--card-black) 0 14px,
        var(--stripe-red) 14px 16px,
        var(--card-black) 16px 22px);
  }

  /* front */
  .brand {
    position: absolute;
    left: 30px; top: 26px;
    display: flex;
    align-items: center;
    gap: 14px;
  }
  .brand-dot {
    width: 42px; height: 42px;
    border-radius: 50%;
    background: var(--text-white);
    flex: none;
  }
  .brand-name {
    font-family: "Open Sans", sans-serif;
    font-weight: 400;
    font-size: 23px;
    line-height: 1.05;
    color: var(--text-white);
    text-align: center;
  }
  .person {
    position: absolute;
    left: 34px; top: 112px;
  }
  .person-name {
    font-size: 26px;
    color: var(--accent-red);
    line-height: 1;
  }
  .person-title {
    font-size: 12px;
    color: var(--text-grey);
    margin-top: 3px;
  }
  .contact {
    position: absolute;
    left: 30px; top: 190px;
    list-style: none;
  }
  .contact li {
    display: flex;
    align-items: center;
    gap: 8px;
    font-size: 12.5px;
    color: var(--text-white);
    height: 18px;
  }
  .contact-icon {
    width: 12px; height: 12px;
    border-radius: 2px;
    background: var(--accent-red);
    color: var(--text-white);
    font-size: 9px;
    display: flex;
    align-items: center;
    justify-content: center;
  }
  .front-lines { position: absolute; left: 0; top: 0; }

  /* back */
  .back-mark {
    position: absolute;
    left: 290px; top: 22px;
    width: 112px; height: 112px;
    border-radius: 50%;
    background: var(--text-white);
  }
  .back-title {
    position: absolute;
    left: 270px; top: 178px;
    transform: translate(-50%, -50%) rotate(25deg);
    white-space: nowrap;
    color: var(--text-white);
  }
  .back-name {
    font-family: "Open Sans", sans-serif;
    font-weight: 600;
    font-size: 28px;
    line-height: 1.2;
  }
  .back-web {
    font-size: 11px;
    margin-top: 6px;
    margin-left: 90px;
  }
</style>
</head>
<body>

  <section class="card card--front" aria-label="Card front">
    <svg class="front-lines" width="540" height="309" viewBox="0 0 540 309" aria-hidden="true">
      <g stroke="var(--stripe-red)" stroke-width="2.5">
        <line x1="440" y1="176" x2="540" y2="176"/>
        <line x1="400" y1="193" x2="540" y2="193"/>
        <line x1="350" y1="210" x2="540" y2="210"/>
        <line x1="290" y1="227" x2="540" y2="227"/>
        <line x1="230" y1="244" x2="540" y2="244"/>
        <line x1="170" y1="261" x2="540" y2="261"/>
        <line x1="0" y1="278" x2="540" y2="278"/>
        <line x1="0" y1="295" x2="540" y2="295"/>
      </g>
    </svg>

    <div class="brand">
      <span class="brand-dot"></span>
      <div class="brand-name">Valdoria International<br>Corporation</div>
    </div>

    <div class="person">
      <div class="person-name">Marnie Dowsett</div>
      <div class="person-title">Purchasing Manager</div>
    </div>

    <ul class="contact">
      <li><span class="contact-icon">p</span>555-317-4086</li>
      <li><span class="contact-icon">f</span>555-241-7953</li>
      <li><span class="contact-icon">e</span>marnie.dowsett@valdoriavic.example</li>
      <li><span class="contact-icon">w</span>www.valdoriavic.example</li>
    </ul>
  </section>

  <section class="card card--back" aria-label="Card back">
    <span class="back-mark"></span>
    <div class="back-title">
      <div class="back-name">Valdoria International Corporation</div>
      <div class="back-web">www.valdoriavic.example</div>
    </div>
  </section>

</body>
</html>
```